Check-up reminder postcard

We require a design for a postcard to remind patients to book their dental check up.

Size: standard postcard 100 x 150mm

We are a small family-focussed dental practice. The design should reflect our brand which is warm & sophisticated as well as incorporate the logo colours. For more information please see our website corrindalefamilydental.com.au.

Target Market(s)

Female aged 30 - 45 years old

Industry/Entity Type

Dental

Requirements
Must have
• The front side should have the copy "We've been missing you...".

Back side of postcard should have area for patient name, address, stamp to be placed. The following copy should be used:

"Dear (please leave space for name)

We've been missing you!

We haven't seen you for your regular dental check up. Please call or visit our website to schedule an appointment. Alternatively, we will be in touch over the next couple of weeks.

We look forward to seeing you again soon!

The Corrindale Family Dental team

Phone: 03 9417 2058 Address: 58 Quenby Parade, Corrindale VIC 3162 Web: www.corrindalefamilydental.com.au Email: admin@corrindalefamilydental.com.au"

Include the logo on back side of postcard. Please add the tag line under the logo "Creating beautiful smiles everyday" - sans serif font.

- Design file:
All colours must be converted to CMYK.
Bleed 3mm external from trim.
Trims and registration marks are offset 5mm.
All text to be 3mm from trim if possible.
Nice to have
• Maple leaf as in the logo
Slightly cursive font
Less cluttered look
Should not have
• Cartoons
Pictures of teeth, drills, probes, mirrors
Photos of people

```html
<!DOCTYPE html>
<html lang="en">
<head>
<meta charset="utf-8">
<title>Corrindale Family Dental – Check-up Reminder Postcard</title>
<link rel="stylesheet" href="https://fonts.googleapis.com/css2?family=Lato:ital,wght@0,400;1,400&display=swap">
<style>
  :root {
    --page-bg: #ece9e3;
    --card-cream: #ebe3cf;
    --card-white: #ffffff;
    --brand-teal: #1a8f96;
    --brand-olive: #9aa51e;
    --text-grey: #6d6b69;
    --rule-grey: #b9b3a6;
  }
  * { margin: 0; padding: 0; box-sizing: border-box; }
  html, body {
    width: 1200px;
    height: 1161px;
    overflow: hidden;
    background: var(--page-bg);
    font-family: "Lato", "Gill Sans", sans-serif;
  }
  .canvas { position: relative; width: 1200px; height: 1161px; }
  .postcard {
    position: absolute;
    left: 305px;
    width: 864px;
    box-shadow: 0 2px 6px rgba(0,0,0,0.18);
    overflow: hidden;
  }
  .postcard--front {
    top: 2px; height: 575px;
    background: linear-gradient(180deg, var(--card-cream) 0%, #efe9da 55%, var(--card-white) 78%, var(--card-white) 100%);
  }
  .postcard--back {
    top: 580px; height: 577px;
    background: linear-gradient(180deg, var(--card-cream) 0%, #efe9da 62%, var(--card-white) 78%, var(--card-white) 100%);
  }

  .brand-dot { position: absolute; border-radius: 50%; background: var(--brand-olive); }
  .brand-name {
    position: absolute;
    color: var(--brand-teal);
    font-weight: 400;
    text-transform: uppercase;
    line-height: 1;
  }
  .brand-name span { display: block; }

  /* Front */
  .postcard--front .brand-dot { left: 30px; top: 280px; width: 110px; height: 110px; }
  .postcard--front .brand-name {
    right: 37px;
    top: 148px;
    text-align: right;
    font-size: 100px;
    letter-spacing: 2px;
  }
  .postcard--front .brand-name span + span { margin-top: 26px; font-size: 82px; letter-spacing: 1px; }
  .front-tagline {
    position: absolute;
    right: 37px;
    top: 446px;
    font-size: 36px;
    font-style: italic;
    color: var(--brand-olive);
  }

  /* Back: logo block */
  .postcard--back .brand-dot { left: 12px; top: 46px; width: 48px; height: 48px; }
  .postcard--back .brand-name { left: 56px; top: 13px; font-size: 36px; letter-spacing: 1px; }
  .postcard--back .brand-name span + span { margin-top: 8px; margin-left: 12px; font-size: 28px; }
  .back-tagline {
    position: absolute;
    left: 58px;
    top: 92px;
    font-size: 17px;
    color: var(--brand-olive);
  }

  /* Back: message */
  .letter {
    position: absolute;
    left: 26px;
    top: 206px;
    font-size: 19px;
    line-height: 27px;
    color: var(--text-grey);
  }
  .letter .signature { margin-top: 22px; font-style: italic; font-size: 18px; }

  /* Back: mailing area */
  .stamp-box {
    position: absolute;
    right: 28px;
    top: 28px;
    width: 92px;
    height: 108px;
    border: 1.5px dashed var(--rule-grey);
    display: flex;
    align-items: center;
    justify-content: center;
    font-size: 14px;
    color: var(--rule-grey);
    text-transform: uppercase;
    letter-spacing: 1px;
  }
  .address-area {
    position: absolute;
    left: 628px;
    top: 230px;
    width: 208px;
  }
  .address-line { height: 40px; border-bottom: 1px solid var(--rule-grey); }

  /* Back: contact */
  .contact {
    position: absolute;
    top: 513px;
    font-size: 18px;
    line-height: 25px;
    color: var(--brand-teal);
  }
  .contact--left { left: 26px; }
  .contact--right { left: 432px; }
</style>
</head>
<body>
<main class="canvas">

  <section class="postcard postcard--front" aria-label="Postcard front">
    <div class="brand-dot" aria-hidden="true"></div>
    <h1 class="brand-name"><span>Corrindale</span><span>Family Dental</span></h1>
    <p class="front-tagline">We've been missing you...</p>
  </section>

  <section class="postcard postcard--back" aria-label="Postcard back">
    <div class="brand-dot" aria-hidden="true"></div>
    <h2 class="brand-name"><span>Corrindale</span><span>Family Dental</span></h2>
    <p class="back-tagline">Creating beautiful smiles everyday</p>

    <div class="stamp-box" aria-label="Stamp area">Stamp</div>

    <div class="address-area" aria-label="Patient address">
      <div class="address-line"></div>
      <div class="address-line"></div>
      <div class="address-line"></div>
      <div class="address-line"></div>
    </div>

    <div class="letter">
      <p>Dear ........................................</p>
      <p>We've been missing you as we haven't seen you<br>
      for your dental check up.<br>
      Over the next couple of weeks we will be in touch otherwise,<br>
      please call or visit our website to book an appointment.<br>
      We look forward to seeing you again soon!</p>
      <p class="signature">The Corrindale Family Dental team</p>
    </div>

    <div class="contact contact--left">
      <p>Phone: 03 9417 2058</p>
      <p>Web: www.corrindalefamilydental.com.au</p>
    </div>
    <div class="contact contact--right">
      <p>Address: 58 Quenby Parade, Corrindale VIC 3162</p>
      <p>Email: admin@corrindalefamilydental.com.au</p>
    </div>
  </section>

</main>
</body>
</html>
```